DL Flyer Design

I need a DL flyer, double-sided designed for a Brisbane based outdoor group exercise/training company called Move Ahead! Move Ahead! provides group outdoor training, designed for the individual. It provides the support, motivation and one-on-one attention of personal training combined with the support of a group environment. The classes are fun, challenging and aim to develop confidence & fitness. Weight loss is not the focus, although it is a benefit.
Updates

Hi

I've just uploaded a high res version of the logo if you need.

Cheers
Tam

Target Market(s)

English speaking men & women aged 25 - 45, white-collar office jobs. Average-low level of fitness, not hugely 'fitness' oriented but want to improve quality of life, overall fitness, lose a bit of weight.

Computer and consumer literate. Live in suburban Brisbane, Australia.

Industry/Entity Type

Training

Requirements
Must have
• Double sided DL. Use of black, greens and white per attached photos. Use of 1300 572 914 (1300 RUN FAR) and website www.movaheadactive.com.au

Indicative copy and contents is posted in the comments section.

```html
<!DOCTYPE html>
<html lang="en">
<head>
<meta charset="utf-8">
<title>Move Ahead! DL Flyer</title>
<link href="https://fonts.googleapis.com/css2?family=Anton&family=Oswald:wght@500;700&display=swap" rel="stylesheet">
<style>
:root{
  --backdrop:#d9d9d6;
  --forest:#1f3a12;
  --moss:#3d6a1c;
  --leaf:#8cc63f;
  --lime:#b8e34c;
  --kelly:#23913a;
  --cream:#f4ecad;
  --ink:#0b0b0b;
  --paper:#ffffff;
  --table-head:#6fb24a;
  --table-line:#b9dca3;
}
*{box-sizing:border-box;margin:0;padding:0}
html,body{width:1200px;height:838px;overflow:hidden}
body{background:var(--backdrop);position:relative;font-family:"Oswald",sans-serif}
.side-label{position:absolute;top:400px;font-family:"Anton",sans-serif;font-size:19px;color:var(--ink);letter-spacing:.5px}
.side-label--front{left:110px}
.side-label--back{left:1020px}
.flyer{position:absolute;top:69px;width:340px;height:700px;overflow:hidden;
  background:linear-gradient(180deg,var(--forest) 0%,#2c4d16 45%,var(--forest) 60%,var(--ink) 100%);
  box-shadow:0 6px 18px rgba(0,0,0,.35)}
.flyer--front{left:250px}
.flyer--back{left:615px}
.flyer > *{position:absolute}
.kicker{top:16px;left:0;width:100%;text-align:center;font-family:"Anton",sans-serif;font-size:17px;color:var(--paper);letter-spacing:.3px}
.hero-art{top:46px;left:0;width:340px;height:300px;
  background:radial-gradient(circle at 32% 30%,#f1e06a 0%,#c9d64a 18%,#6f8f2a 42%,#2f4d17 70%,var(--forest) 100%)}
.intro{top:150px;left:36px;font-family:"Anton",sans-serif;font-size:24px;color:var(--paper);transform:rotate(-3deg)}
.brand-name{top:186px;left:100px;font-family:"Anton",sans-serif;font-size:60px;line-height:.95;color:var(--lime)}
.tagline{top:340px;left:0;width:100%;text-align:center;font-family:"Anton",sans-serif;font-size:18px;line-height:1.15;color:var(--paper);transform:rotate(2deg)}
.base-curve{left:0;width:340px}
.flyer--front .base-curve{top:380px;height:320px}
.flyer--back .base-curve{top:385px;height:315px}
.pitch{top:425px;left:30px;width:280px;text-align:center;font-weight:700;font-size:10.5px;line-height:1.2;color:var(--cream);text-transform:uppercase}
.pitch p + p{margin-top:6px;font-size:12px}
.offer{top:555px;left:0;width:100%;text-align:center;font-family:"Anton",sans-serif;font-size:17px;line-height:1.15;color:var(--paper)}
.offer small{display:block;font-family:"Oswald",sans-serif;font-size:6.5px;font-weight:500}
.contact-front{top:622px;left:0;width:100%;text-align:center;color:var(--cream);font-weight:700;text-transform:uppercase}
.contact-front .call{font-size:12.5px;line-height:1.1}
.contact-front .web{font-size:8.5px;margin-top:4px;line-height:1.2}
.schedule{top:410px;left:14px;width:312px;border:2px solid var(--table-head);border-collapse:collapse;font-size:7px;color:#2b4a1e;background:var(--paper)}
.schedule th{background:var(--table-head);color:var(--paper);font-weight:500;text-align:left;padding:2px 3px}
.schedule td{padding:2px 3px;vertical-align:top;height:16px;border-top:1px solid var(--table-line)}
.schedule tr.alt td{background:#e3f1d8}
.mountain-art{top:520px;left:0;width:340px;height:70px;background:linear-gradient(180deg,#ffffff 0%,#ececec 60%,#ffffff 100%)}
.contact-back{top:528px;left:0;width:100%;text-align:center;font-family:"Anton",sans-serif;text-transform:uppercase}
.contact-back .call-now{font-size:22px;color:var(--ink)}
.contact-back .number{font-size:22px;line-height:1.05;color:var(--kelly)}
.contact-back .number span{font-size:12px;color:var(--ink)}
.contact-back .web{font-family:"Oswald",sans-serif;font-weight:700;font-size:10px;color:var(--ink);margin-top:8px;line-height:1.3}
</style>
</head>
<body>
<div class="side-label side-label--front">FRONT</div>
<div class="side-label side-label--back">BACK</div>

<section class="flyer flyer--front">
  <div class="hero-art" role="img" aria-label="Outdoor scene: glowing sun, birds, bicycle, tree and a leaping runner silhouette against a stone wall"></div>
  <h2 class="kicker">TIRED OF HANGING ABOUT?</h2>
  <div class="intro">IT'S TIME TO</div>
  <div class="brand-name">Move<br>Ahead!</div>
  <svg class="base-curve" viewBox="0 0 340 320" preserveAspectRatio="none" aria-hidden="true">
    <path d="M0 170 Q170 110 340 0 L340 320 L0 320 Z" fill="var(--ink)"/>
  </svg>
  <h3 class="tagline">WITH GROUP OUTDOOR TRAINING<br>DESIGNED JUST FOR YOU.</h3>
  <div class="pitch">
    <p>Move Ahead! provides the unique combination of the one-on-one attention of personal training with the motivation and support of a group environment.</p>
    <p>Best of all, it's designed to fit fitness into your life - at an affordable price.</p>
  </div>
  <div class="offer">CURIOUS? GIVE IT A SHOT<br>WITH A 1 WEEK FREE TRIAL!<small>(GUARANTEED NO HARD SELL AT THE END)</small></div>
  <div class="contact-front">
    <div class="call">Call now<br>on 1300 RUN FAR (1300 572 914)</div>
    <div class="web">Email hello@movaheadactive.com.au or<br>www.movaheadactive.com.au</div>
  </div>
</section>

<section class="flyer flyer--back">
  <div class="hero-art" role="img" aria-label="Outdoor scene: glowing sun, birds, bicycle, tree and a leaping runner silhouette against a stone wall"></div>
  <h2 class="kicker">TIRED OF HANGING ABOUT?</h2>
  <div class="intro">IT'S TIME TO</div>
  <div class="brand-name">Move<br>Ahead!</div>
  <svg class="base-curve" viewBox="0 0 340 315" preserveAspectRatio="none" aria-hidden="true">
    <path d="M0 80 Q200 40 340 0 L340 315 L0 315 Z" fill="var(--paper)"/>
  </svg>
  <h3 class="tagline">WITH GROUP OUTDOOR TRAINING<br>DESIGNED JUST FOR YOU.</h3>
  <table class="schedule">
    <tr><th>Time</th><th>Monday</th><th>Tuesday</th><th>Wednesday</th><th>Thursday</th><th>Friday</th><th>Saturday</th></tr>
    <tr class="alt"><td><b>6.00am</b></td><td>Cardio</td><td></td><td>Stress-relief (boxing!)</td><td>Cardio</td><td>Stress-relief (boxing!)</td><td>Mash-up</td></tr>
    <tr><td></td><td></td><td></td><td></td><td></td><td></td><td>One-on-One sessions</td></tr>
    <tr class="alt"><td><b>6.00pm</b></td><td>Strength</td><td>Cardio</td><td>Strength</td><td>Stress-relief (boxing!)</td><td></td><td></td></tr>
  </table>
  <div class="mountain-art" role="img" aria-label="Faint snowy mountain range behind the contact details"></div>
  <div class="contact-back">
    <div class="call-now">CALL NOW</div>
    <div class="number">ON 1300 RUN FAR<br>(1300 572 914) <span>OR</span></div>
    <div class="web">EMAIL HELLO@MOVAHEADACTIVE.COM.AU.<br>WWW.MOVAHEADACTIVE.COM.AU</div>
  </div>
</section>
</body>
</html>
```